VS Business Card

Design new business cards for VELNAstack

Please see attached for the design brief

**** Please note, please feel free to propose a font that works for a professional, technology company ***

Target Market(s)

Technology buyers

Industry/Entity Type

Business

```html
<!DOCTYPE html>
<html lang="en">
<head>
<meta charset="utf-8">
<title>Velnastack Business Card</title>
<link href="https://fonts.googleapis.com/css2?family=Ubuntu:wght@400;500;700&display=swap" rel="stylesheet">
<style>
  :root {
    --navy-dark: #0b1626;
    --navy-band: #2b3a7c;
    --brand-blue: #3a4f93;
    --name-blue: #1f2f6b;
    --title-blue: #5b7fc2;
    --paper: #ececec;
    --orange: #e39a25;
    --teal: #2a8a78;
    --white: #f4f5f7;
    --muted: #c9cfe0;
    --backdrop: #d9d6d1;
  }
  * { margin: 0; padding: 0; box-sizing: border-box; }
  html, body { width: 1200px; height: 1000px; overflow: hidden; }
  body {
    background: var(--backdrop);
    font-family: "Ubuntu", Arial, sans-serif;
    position: relative;
  }
  .card {
    position: absolute;
    left: 160px;
    width: 880px;
    height: 460px;
    overflow: hidden;
    box-shadow: 0 6px 18px rgba(0,0,0,0.18);
  }
  /* Back side */
  .card-back { top: 30px; background: var(--navy-dark); }
  .card-back .band {
    position: absolute; left: 0; right: 0; top: 372px; height: 60px;
    background: var(--navy-band);
    display: flex; align-items: center; justify-content: center;
  }
  .card-back .website { color: var(--muted); font-size: 22px; letter-spacing: 0.5px; }
  .brand { position: absolute; display: flex; flex-direction: column; }
  .card-back .brand { left: 50%; top: 150px; transform: translateX(-50%); align-items: center; }
  .brand-name { font-weight: 500; color: var(--brand-blue); font-size: 60px; letter-spacing: 1px; line-height: 1; }
  .tagline { color: var(--muted); font-size: 18px; margin-top: 12px; }
  /* Front side */
  .card-front { top: 510px; background: var(--paper); }
  .card-front svg.sweep { position: absolute; inset: 0; }
  .card-front .brand { right: 30px; top: 26px; align-items: flex-end; }
  .card-front .brand-name { font-size: 30px; letter-spacing: 0.5px; }
  .card-front .tagline { color: var(--name-blue); font-size: 11px; margin-top: 5px; }
  .holder { position: absolute; left: 64px; top: 180px; }
  .holder-name { color: var(--name-blue); font-weight: 700; font-size: 40px; }
  .holder-title { color: var(--title-blue); font-weight: 700; font-size: 34px; margin-left: 150px; margin-top: 2px; }
  .address { position: absolute; left: 410px; top: 318px; color: var(--white); font-size: 19px; line-height: 1.3; }
  .address .company { color: var(--teal); }
  .contacts { position: absolute; left: 600px; top: 188px; list-style: none; color: var(--white); font-size: 16px; line-height: 1.55; }
  .contacts li { display: flex; align-items: center; gap: 10px; }
  .contacts svg { width: 16px; height: 16px; fill: var(--orange); flex: none; }
</style>
</head>
<body>

<section class="card card-back" aria-label="Business card back">
  <div class="brand">
    <span class="brand-name">Velnastack</span>
    <span class="tagline">built for what comes next</span>
  </div>
  <div class="band"><span class="website">www.velnastack-it.com</span></div>
</section>

<section class="card card-front" aria-label="Business card front">
  <svg class="sweep" viewBox="0 0 880 460" width="880" height="460" aria-hidden="true">
    <path d="M300 460 C360 270 560 150 880 125 L880 460 Z" fill="var(--navy-dark)"/>
    <path d="M262 460 C322 250 540 120 880 95" fill="none" stroke="var(--orange)" stroke-width="6"/>
  </svg>

  <div class="brand">
    <span class="brand-name">Velnastack</span>
    <span class="tagline">built for what comes next</span>
  </div>

  <div class="holder">
    <div class="holder-name">Lukas BRENNER</div>
    <div class="holder-title">CEO</div>
  </div>

  <div class="address">
    <div class="company">Velnastack Solutions AG</div>
    <div>Lindenweg 8</div>
    <div>6300 Zug</div>
    <div>Switzerland</div>
  </div>

  <ul class="contacts">
    <li><svg viewBox="0 0 16 16"><path d="M3 1h3l1 4-2 1a9 9 0 0 0 5 5l1-2 4 1v3a2 2 0 0 1-2 2A13 13 0 0 1 1 3a2 2 0 0 1 2-2z"/></svg>+41 41 555 01 20 / 21</li>
    <li><svg viewBox="0 0 16 16"><path d="M4 1h8v4H4zM1 6h14v6h-3v3H4v-3H1zM5 10v4h6v-4z"/></svg>+41 80 555 01 72</li>
    <li><svg viewBox="0 0 16 16"><path d="M4 0h8a1 1 0 0 1 1 1v14a1 1 0 0 1-1 1H4a1 1 0 0 1-1-1V1a1 1 0 0 1 1-1zm1 2v10h6V2zm3 11a1 1 0 1 0 0 2 1 1 0 0 0 0-2z"/></svg>+41 78 555 01 98</li>
    <li><svg viewBox="0 0 16 16"><path d="M0 3h16v10H0zM1 4l7 5 7-5H1z"/></svg>lukas.brenner@velnastack-it.com</li>
  </ul>
</section>

</body>
</html>
```